Visitenkarten-Design für modernes Industrieunternehmen
Zielgruppe
Wir stellen loses Füllmaterial (Schaumstoff-sticks, Latex-sticks und Visco-sticks) für Kopfkissen und Polstermöbel her. Auch Füllungen für Gartenauflagen sind in unserem Repertoire.
Aufgabenstellung
Wir liefern nicht an Endkunden, sondern nur an andere Unternehmen. Die Visitenkarte soll daher eine gewisse Seriösität ausstrahlen, aber trotzdem ins Auge fallen.

```html
<!DOCTYPE html>
<html lang="de">
<head>
<meta charset="utf-8">
<title>Fillora – Visitenkarten</title>
<link rel="stylesheet" href="https://fonts.googleapis.com/css2?family=Open+Sans:wght@400;600;700&display=swap">
<style>
  :root {
    --brand-blue: #0b67a3;
    --brand-grey: #8f8f8f;
    --paper: #ffffff;
    --ink: #1c1c1c;
    --stage: #3b3e42;
  }
  * { box-sizing: border-box; margin: 0; padding: 0; }
  html, body { width: 1200px; height: 800px; overflow: hidden; }
  body {
    background: var(--stage);
    font-family: "Open Sans", Arial, sans-serif;
    display: flex;
    align-items: center;
    justify-content: center;
    gap: 60px;
  }
  .card {
    position: relative;
    width: 520px;
    height: 336px;
    overflow: hidden;
    box-shadow: 0 10px 30px rgba(0,0,0,.45);
  }

  /* Front */
  .card--front { background: var(--paper); color: var(--ink); }
  .name-marker {
    position: absolute; left: 0; top: 34px;
    width: 16px; height: 30px; background: var(--brand-blue);
  }
  .person { position: absolute; left: 38px; top: 32px; }
  .person__name { font-size: 21px; font-weight: 700; color: var(--brand-blue); line-height: 1.1; }
  .person__role { font-size: 13px; color: var(--ink); margin-top: 2px; }

  .brand { position: absolute; }
  .brand__name { font-weight: 600; letter-spacing: 2px; line-height: 1; white-space: nowrap; }
  .card--front .brand { right: 44px; top: 118px; }
  .card--front .brand__name { font-size: 46px; color: var(--brand-blue); }

  .contact { position: absolute; left: 40px; top: 190px; list-style: none; }
  .contact__item { display: flex; align-items: center; gap: 10px; font-size: 14px; line-height: 20px; white-space: nowrap; }
  .contact__icon { width: 14px; height: 14px; fill: var(--brand-blue); flex: none; }

  .address {
    position: absolute; right: 44px; top: 230px;
    font-size: 15px; font-style: normal; text-align: right; line-height: 21px;
  }
  .base-bands { position: absolute; left: 0; bottom: 0; width: 520px; height: 28px; }

  /* Back */
  .card--back { background: var(--brand-blue); color: var(--paper); }
  .card--back .brand { right: 48px; top: 130px; }
  .card--back .brand__name { font-size: 50px; color: var(--paper); }
  .card--back .website {
    position: absolute; right: 48px; bottom: 40px;
    font-size: 13px; letter-spacing: 3px;
  }
</style>
</head>
<body>

  <section class="card card--front" aria-label="Visitenkarte Vorderseite">
    <div class="name-marker"></div>
    <div class="person">
      <p class="person__name">Jonas Kerwald</p>
      <p class="person__role">Geschäftsführer</p>
    </div>

    <div class="brand">
      <span class="brand__name">Fillora</span>
    </div>

    <ul class="contact">
      <li class="contact__item">
        <svg class="contact__icon" viewBox="0 0 16 16" aria-hidden="true"><path d="M3 1l3 3-1.5 2c1 2 3 4 5.5 5.5l2-1.5 3 3-2 2C7 15 1 9 1 3z"/></svg>
        +49 (0) 12 34 / 56 78 90
      </li>
      <li class="contact__item">
        <svg class="contact__icon" viewBox="0 0 16 16" aria-hidden="true"><path d="M4 1h8v4H4zM1 6h14v6h-3v3H4v-3H1zM5 10v4h6v-4z"/></svg>
        +49 (0) 12 34 / 56 78 91
      </li>
      <li class="contact__item">
        <svg class="contact__icon" viewBox="0 0 16 16" aria-hidden="true"><path d="M1 3h14v10H1zM2 4l6 5 6-5v-.5H2z" fill-rule="evenodd"/></svg>
        info@fillora.info
      </li>
      <li class="contact__item">
        <svg class="contact__icon" viewBox="0 0 16 16" aria-hidden="true"><circle cx="8" cy="8" r="7"/><path d="M1 8h14M8 1c-3 3-3 11 0 14M8 1c3 3 3 11 0 14" stroke="#fff" stroke-width="1" fill="none"/></svg>
        www.fillora.com
      </li>
    </ul>

    <address class="address">
      Ahornweg 12<br>12345 Musterstadt
    </address>

    <svg class="base-bands" viewBox="0 0 520 28" aria-hidden="true">
      <polygon points="0,0 360,0 366,28 0,28" fill="var(--brand-grey)"/>
      <polygon points="368,0 376,0 382,28 374,28" fill="var(--brand-blue)"/>
      <polygon points="382,0 390,0 396,28 388,28" fill="var(--brand-blue)"/>
      <polygon points="396,0 520,0 520,28 402,28" fill="var(--brand-blue)"/>
    </svg>
  </section>

  <section class="card card--back" aria-label="Visitenkarte Rückseite">
    <div class="brand">
      <span class="brand__name">Fillora</span>
    </div>
    <p class="website">www.fillora.com</p>
  </section>

</body>
</html>
```